Design an Infographic for Teamzo - the hub for clubs

We need an infographic for our start up company "Teamzo". We've recently re-branded and we'd like a simple design with our new logo incorporated. Teamzo is a fun yet professional online portal that helps schools to run all of their extra curricular activities, it saves the school time and money.We want to use this infographic to improve our brand presence and as a marketing tool.Please use attached logo and colour palette.

Requirements
Must have
• Be editable so we can update the template in the future.
Nice to have
• Some ideas for stats:
• How many schools we're working with
• How many children have been inspired
• No. of activities we offer
• No. of users
• Feedback
• Attendance %
• Regional Coverage

```html
<!DOCTYPE html>
<html lang="en">
<head>
<meta charset="utf-8">
<title>Teamzo – The Hub for Clubs</title>
<link rel="stylesheet" href="https://fonts.googleapis.com/css2?family=Roboto+Condensed:ital,wght@0,400;0,700;1,700&display=swap">
<style>
:root{
  --purple:#92278f;
  --magenta:#a3237e;
  --lime:#bfd643;
  --blue:#4f74b5;
  --yellow:#e1d34a;
  --red:#e2302d;
  --grey:#9a9a9a;
  --light-grey:#e6e6e8;
  --sky:#64c4ea;
  --teal:#5ac2d1;
  --rose:#d9365f;
  --ink:#1a1a1a;
  --orange:#f08a3c;
}
*{margin:0;padding:0;box-sizing:border-box}
html,body{width:776px;height:1200px;overflow:hidden;background:#fff}
body{font-family:"Roboto Condensed",Arial,sans-serif;color:var(--ink);position:relative}
.abs{position:absolute}
.header{position:absolute;left:0;top:0;width:776px;height:130px}
.header-left{position:absolute;left:0;top:0;width:278px;height:130px;background:linear-gradient(180deg,#efeff1,#dcdce0)}
.header-right{position:absolute;left:278px;top:0;width:498px;height:130px;background:linear-gradient(180deg,#a0329d,#8a2387)}
.brand{position:absolute;left:62px;top:40px;display:flex;align-items:center;gap:8px}
.brand-dot{width:26px;height:26px;border-radius:50%;background:var(--purple)}
.brand-name{font-size:40px;font-weight:700;color:var(--purple);line-height:1}
.brand-tag{position:absolute;left:96px;top:88px;font-size:15px;font-weight:700;color:var(--purple)}
.title{position:absolute;left:278px;width:498px;text-align:center;color:#fff;font-weight:700}
.title-main{top:30px;font-size:46px;letter-spacing:-1px}
.title-sub{top:78px;font-size:32px;font-style:italic}
.sec-head{position:absolute;left:72px;font-size:16px;font-weight:700;color:var(--magenta);text-transform:uppercase;letter-spacing:-.2px}
.divider{position:absolute;left:72px;width:634px;border-top:3px dotted #b8b8b8}
.stat{position:absolute;left:72px;display:flex;align-items:flex-start;gap:8px;font-size:13px;font-weight:700;line-height:1.2}
.stat .num{font-size:21px;font-weight:700;line-height:1;min-width:44px}
.stat .num small{font-size:11px}
.legend{position:absolute;display:flex;gap:12px;font-size:8px;font-weight:700;align-items:center;line-height:1}
.legend span{display:flex;align-items:center;gap:4px}
.legend i{display:inline-block;width:9px;height:9px}
.bar{position:absolute;display:flex;height:16px;font-size:13px;color:#fff;line-height:1}
.bar div{display:flex;align-items:center;justify-content:center}
.bar-label{position:absolute;font-size:10px;font-weight:700;white-space:nowrap}
.callout{position:absolute;left:72px;top:568px;width:174px;height:112px;background:var(--yellow);color:#fff;font-size:9.5px;font-weight:700;padding:6px 8px;line-height:1.15}
.callout p{margin-bottom:6px}
.users-label{position:absolute;right:272px;font-size:9.5px;font-weight:700;text-align:right;line-height:1.2}
.fb-text{position:absolute;left:385px;top:745px;width:170px;text-align:center;font-size:17px;font-weight:700;line-height:1.2}
.att-text{position:absolute;left:385px;font-size:12.5px;font-weight:700}
.reg-text{position:absolute;left:72px;width:320px;font-size:9.5px;font-weight:700;line-height:1.35}
.footer-line{position:absolute;left:72px;top:1100px;width:634px;border-top:1.5px solid var(--orange)}
.copy{position:absolute;left:0;width:776px;top:1116px;text-align:center;font-size:10px;font-weight:700;color:#555}
.chart-val{font-size:10px;font-weight:700;fill:var(--ink)}
</style>
</head>
<body>

<header class="header">
  <div class="header-left"></div>
  <div class="header-right" role="img" aria-label="Faint silhouettes of a crowd of people across the purple banner"></div>
  <div class="brand"><div class="brand-dot"></div><div class="brand-name">Teamzo</div></div>
  <div class="brand-tag">The hub for clubs</div>
  <div class="title title-main">THE HUB FOR CLUBS</div>
  <div class="title title-sub">(LOREM IPSUM)</div>
</header>

<!-- Schools -->
<div class="sec-head" style="top:147px">Schools we're working with</div>
<div class="stat" style="top:180px;width:320px"><span class="num">46<small>%</small></span><span>of students believe boys and girls are treated differently.</span></div>
<div class="stat" style="top:213px;width:320px"><span class="num">58<small>%</small></span><span>of students do not believe students are treated the same.</span></div>
<svg class="abs" style="left:436px;top:140px" width="300" height="108">
  <circle cx="47" cy="45" r="36" fill="none" stroke="var(--light-grey)" stroke-width="12"/>
  <circle cx="47" cy="45" r="36" fill="none" stroke="var(--sky)" stroke-width="12" stroke-dasharray="104 226" transform="rotate(-90 47 45)"/>
  <text x="47" y="52" text-anchor="middle" font-size="20" font-weight="700">46<tspan font-size="10">%</tspan></text>
  <text x="47" y="100" text-anchor="middle" font-size="12" font-weight="700">Differently</text>
  <rect x="108" y="31" width="12" height="10" fill="var(--sky)"/>
  <text x="125" y="40" font-size="9" font-weight="700">AGREE</text>
  <rect x="108" y="50" width="12" height="10" fill="var(--light-grey)"/>
  <text x="125" y="59" font-size="9" font-weight="700">DISAGREE</text>
  <circle cx="222" cy="45" r="36" fill="none" stroke="var(--light-grey)" stroke-width="12"/>
  <circle cx="222" cy="45" r="36" fill="none" stroke="var(--sky)" stroke-width="12" stroke-dasharray="131 226" transform="rotate(-90 222 45)"/>
  <text x="222" y="52" text-anchor="middle" font-size="20" font-weight="700">58<tspan font-size="10">%</tspan></text>
  <text x="222" y="100" text-anchor="middle" font-size="12" font-weight="700">The Same</text>
</svg>
<div class="divider" style="top:246px"></div>

<!-- Children inspired -->
<div class="sec-head" style="top:256px">Children have been inspired</div>
<div class="stat" style="top:292px;width:340px"><span class="num">82<small>%</small></span><span>of the students felt like the teachers communicate effectively when they have misbehaved</span></div>
<div class="stat" style="top:337px;width:340px"><span class="num">45<small>%</small></span><span>believe that discipline is not fair and 53% believe that the rules are not applied equally</span></div>
<svg class="abs" style="left:490px;top:270px" width="230" height="108">
  <rect x="9" y="22" width="24" height="58" fill="var(--lime)"/>
  <rect x="39" y="32" width="24" height="48" fill="var(--blue)"/>
  <rect x="108" y="24" width="24" height="56" fill="var(--lime)"/>
  <rect x="138" y="36" width="24" height="44" fill="var(--blue)"/>
  <line x1="2" y1="80" x2="175" y2="80" stroke="#333" stroke-width="1"/>
  <text class="chart-val" x="21" y="18" text-anchor="middle" font-size="12">55%</text>
  <text class="chart-val" x="51" y="28" text-anchor="middle" font-size="12">45%</text>
  <text class="chart-val" x="120" y="20" text-anchor="middle" font-size="12">53%</text>
  <text class="chart-val" x="150" y="32" text-anchor="middle" font-size="12">47%</text>
  <text x="36" y="92" text-anchor="middle" font-size="8" font-weight="700">Discipline is fair</text>
  <text x="135" y="92" text-anchor="middle" font-size="8" font-weight="700">Rules are applied equally</text>
  <text x="135" y="102" text-anchor="middle" font-size="8" font-weight="700">to all students</text>
  <rect x="195" y="49" width="9" height="9" fill="var(--lime)"/><text x="208" y="57" font-size="8" font-weight="700">YES</text>
  <rect x="195" y="67" width="9" height="9" fill="var(--blue)"/><text x="208" y="75" font-size="8" font-weight="700">NO</text>
</svg>
<div class="divider" style="top:378px"></div>

<!-- Activities -->
<div class="sec-head" style="top:386px">Activities we offer</div>
<div class="bar" style="left:72px;top:408px;width:198px"><div style="width:78.85%;background:var(--purple)">78.85%</div><div style="flex:1;background:var(--grey)">21.14%</div></div>
<div class="bar" style="left:72px;top:427px;width:198px"><div style="width:80.46%;background:var(--purple)">80.46%</div><div style="flex:1;background:var(--grey)">19.54%</div></div>
<div class="bar" style="left:72px;top:446px;width:198px"><div style="width:90.17%;background:var(--purple)">90.17%</div><div style="flex:1;background:var(--grey)">9.83%</div></div>
<div class="bar" style="left:72px;top:465px;width:198px"><div style="width:74.42%;background:var(--purple)">74.42%</div><div style="flex:1;background:var(--grey)">25.59%</div></div>
<div class="bar" style="left:72px;top:484px;width:198px"><div style="width:85.64%;background:var(--purple)">85.64%</div><div style="flex:1;background:var(--grey)">14.36%</div></div>
<div class="bar" style="left:72px;top:503px;width:198px"><div style="width:76%;background:var(--purple)">76%</div><div style="flex:1;background:var(--grey)">24%</div></div>
<div class="bar-label" style="left:277px;top:410px">My teachers really care about me</div>
<div class="bar-label" style="left:277px;top:429px">My teachers give me individual attention when I need it</div>
<div class="bar-label" style="left:277px;top:448px">If I am absent, there is a teacher or some other adult at school that will notice my absence</div>
<div class="bar-label" style="left:277px;top:467px">My teachers make me feel good about myself</div>
<div class="bar-label" style="left:277px;top:486px">My teachers are about me</div>
<div class="bar-label" style="left:277px;top:505px">Teachers are available when I need to talk with them and they are easy to talk with</div>
<div class="legend" style="left:136px;top:524px"><span><i style="background:var(--purple)"></i>YES</span><span><i style="background:var(--grey)"></i>NO</span></div>
<div class="divider" style="top:540px"></div>

<!-- Users -->
<div class="sec-head" style="top:546px">Users</div>
<div class="callout">
  <p>36% to 38% of the students do not feel positive behavior while at school</p>
  <p>30% do not believe they are respected by adults</p>
  <p>30% do not believe they can talk about personal problems</p>
  <p>50% do not believe teachers understand their problems</p>
</div>
<div class="users-label" style="top:570px;width:250px">Adults working at this school reward students for positive behavior.</div>
<div class="users-label" style="top:602px;width:250px">Adult working at this school treat all students respectfully.</div>
<div class="users-label" style="top:619px;width:250px">I can talk to teacher or other adult at this school about something that is bothering me.</div>
<div class="users-label" style="top:648px;width:250px">Teachers understand my problems.</div>
<div class="users-label" style="top:666px;width:250px">My teachers praise me when I work hard in school.</div>
<div class="bar" style="left:512px;top:567px;width:194px;height:17px"><div style="width:78.85%;background:var(--yellow)">78.85%</div><div style="flex:1;background:var(--grey)">21.14%</div></div>
<div class="bar" style="left:512px;top:586px;width:194px;height:17px"><div style="width:80.46%;background:var(--yellow)">80.46%</div><div style="flex:1;background:var(--grey)">19.54%</div></div>
<div class="bar" style="left:512px;top:605px;width:194px;height:17px"><div style="width:90.17%;background:var(--yellow)">90.17%</div><div style="flex:1;background:var(--grey)">9.83%</div></div>
<div class="bar" style="left:512px;top:624px;width:194px;height:17px"><div style="width:74.42%;background:var(--yellow)">74.42%</div><div style="flex:1;background:var(--grey)">25.59%</div></div>
<div class="bar" style="left:512px;top:643px;width:194px;height:17px"><div style="width:85.64%;background:var(--yellow)">85.64%</div><div style="flex:1;background:var(--grey)">14.36%</div></div>
<div class="bar" style="left:512px;top:662px;width:194px;height:17px"><div style="width:76%;background:var(--yellow)">76%</div><div style="flex:1;background:var(--grey)">24%</div></div>
<div class="legend" style="left:578px;top:684px"><span><i style="background:var(--yellow)"></i>YES</span><span><i style="background:var(--grey)"></i>NO</span></div>
<div class="divider" style="top:697px"></div>

<!-- Feedback -->
<div class="sec-head" style="top:704px">Feedback</div>
<svg class="abs" style="left:72px;top:725px" width="310" height="125">
  <line x1="0.5" y1="0" x2="0.5" y2="121" stroke="#333"/>
  <line x1="0" y1="120.5" x2="310" y2="120.5" stroke="#333"/>
  <rect x="33" y="104" width="45" height="16" fill="var(--yellow)"/>
  <rect x="88" y="22" width="45" height="98" fill="var(--purple)"/>
  <rect x="143" y="7" width="47" height="113" fill="var(--lime)"/>
  <rect x="199" y="66" width="45" height="54" fill="var(--blue)"/>
  <rect x="254" y="75" width="46" height="45" fill="var(--rose)"/>
  <text x="55" y="116" text-anchor="middle" font-size="9" font-weight="700" fill="#fff">5.14%</text>
  <text x="110" y="44" text-anchor="middle" font-size="11" font-weight="700" fill="#fff">30.86%</text>
  <text x="166" y="25" text-anchor="middle" font-size="11" font-weight="700" fill="#fff">36.00%</text>
  <text x="221" y="80" text-anchor="middle" font-size="11" font-weight="700" fill="#fff">15.43%</text>
  <text x="277" y="89" text-anchor="middle" font-size="11" font-weight="700" fill="#fff">12.57%</text>
</svg>
<div class="fb-text">64% of the students do not feel like students like one another</div>
<svg class="abs" style="left:568px;top:722px" width="120" height="125">
  <circle cx="57" cy="55" r="54" fill="var(--teal)"/>
  <path d="M57 55 L47.6 1.8 A54 54 0 0 1 104 81.7 Z" fill="#e4e4e6"/>
  <text x="38" y="80" text-anchor="middle" font-size="26" font-weight="700" fill="#fff">64<tspan font-size="12">%</tspan></text>
  <text x="76" y="40" text-anchor="middle" font-size="18" font-weight="700" fill="var(--ink)">36<tspan font-size="10"> %</tspan></text>
  <rect x="28" y="115" width="9" height="9" fill="var(--purple)"/><text x="41" y="123" font-size="8" font-weight="700">YES</text>
  <rect x="60" y="115" width="9" height="9" fill="#e4e4e6"/><text x="73" y="123" font-size="8" font-weight="700">NO</text>
</svg>
<div class="divider" style="top:855px"></div>

<!-- Attendance -->
<div class="sec-head" style="top:864px">Attendance %</div>
<div class="bar" style="left:72px;top:890px;width:298px;height:17px"><div style="width:64%;background:var(--red)">79.43%</div><div style="flex:1;background:var(--grey)">20.57%</div></div>
<div class="bar" style="left:72px;top:910px;width:298px;height:17px"><div style="width:63%;background:var(--red)">78.74%</div><div style="flex:1;background:var(--grey)">21.26%</div></div>
<div class="bar" style="left:72px;top:930px;width:298px;height:17px"><div style="width:68%;background:var(--red)">81.72%</div><div style="flex:1;background:var(--grey)">18.28%</div></div>
<div class="att-text" style="top:893px">I feel I belong.</div>
<div class="att-text" style="top:911px">I feel I like belong and I am a part of this school.</div>
<div class="att-text" style="top:929px">I feel socially accepted.</div>
<div class="legend" style="left:136px;top:951px"><span><i style="background:var(--red)"></i>YES</span><span><i style="background:var(--grey)"></i>NO</span></div>
<div class="divider" style="top:967px"></div>

<!-- Regional coverage -->
<div class="sec-head" style="top:978px">Regional coverage</div>
<div class="reg-text" style="top:1004px">I regularly participate in Extra-Curricular activities offered through this school, such as, school clubs or Organizations, Musical Groups, Sports Teams, Student Government, or any other Extra-Curricular activities.</div>
<div class="reg-text" style="top:1058px">I regularly attend school-sponsored events, such as school dances, sporting events, student performances, or other school activities.</div>
<div class="bar" style="left:420px;top:1008px;width:288px;height:26px;font-size:15px"><div style="width:70%;background:var(--lime)">83.42%</div><div style="flex:1;background:var(--purple);justify-content:flex-end;padding-right:4px;font-size:11px">16.58%</div></div>
<div class="bar" style="left:420px;top:1046px;width:288px;height:26px;font-size:15px"><div style="width:65%;background:var(--lime)">76.44%</div><div style="flex:1;background:var(--purple);justify-content:flex-end;padding-right:4px;font-size:11px">23.56%</div></div>
<div class="legend" style="left:540px;top:1079px"><span><i style="background:var(--lime)"></i>YES</span><span><i style="background:var(--purple)"></i>NO</span></div>

<div class="footer-line"></div>
<div class="copy">© 2019 All Rights Reserved.</div>

</body>
</html>
```